Hi, We are global cloud printer looking to start a ad print run, we require full and half page print ad's designed with the following dimensions

Full page dimensions:

Image area: 345 mm in height x 260 mm (6 columns) in width
Trim area: 368 mm in height x 280 mm (6 columns) in width
Bleed area: 371 mm in height x 283 mm (6 columns) in width

Half-page dimensions:
270 mm in height x 172 mm (4 columns) in width

We want a minimalistic ad that really stands out from the crowd, with a full page we want it to make an impact and drive people towards our site.

The site is www.plaventro.com , we would like to match the look and feel but would like the wow factor so our open to all concepts.

We would like the following tagline incorporated in the Ad The cloud you've been waiting for, might be closer than you think.

```html
<!DOCTYPE html>
<html lang="en">
<head>
<meta charset="utf-8">
<title>Plaventro – Enterprise SSD Cloud</title>
<link rel="stylesheet" href="https://fonts.googleapis.com/css2?family=Fira+Sans+Condensed:wght@600&family=Signika:wght@400;500&display=swap">
<style>
  :root {
    --frame: #777777;
    --paper-light: #ececec;
    --paper-mid: #dedede;
    --paper-dark: #cfcfcf;
    --slate: #3a4a56;
    --lime: #8cc63f;
    --lime-soft: #c9dfae;
    --slate-soft: #b9c0c5;
  }
  * { margin: 0; padding: 0; box-sizing: border-box; }
  html, body {
    width: 914px;
    height: 1200px;
    overflow: hidden;
    background: var(--frame);
  }
  .ad {
    position: relative;
    width: 914px;
    height: 1200px;
    background: var(--frame);
  }
  .paper {
    position: absolute;
    left: 32px;
    top: 32px;
    width: 850px;
    height: 1136px;
    background:
      radial-gradient(ellipse at 30% 25%, var(--paper-light) 0%, transparent 60%),
      radial-gradient(ellipse at 75% 70%, var(--paper-light) 0%, transparent 55%),
      linear-gradient(160deg, var(--paper-mid) 0%, var(--paper-light) 45%, var(--paper-dark) 100%);
  }
  .brand {
    position: absolute;
    left: 0;
    top: 92px;
    width: 914px;
    text-align: center;
    font-family: "Signika", sans-serif;
    font-weight: 500;
    font-size: 120px;
    line-height: 1;
    letter-spacing: -1px;
    color: var(--slate);
  }
  .cloud-art {
    position: absolute;
    left: 296px;
    top: 472px;
    width: 306px;
    height: 186px;
    border-radius: 93px;
    background: radial-gradient(ellipse at 50% 45%, var(--lime-soft) 0%, var(--slate-soft) 100%);
  }
  .slogan {
    position: absolute;
    left: 0;
    top: 760px;
    width: 914px;
    text-align: center;
    font-family: "Signika", sans-serif;
    font-weight: 400;
    font-size: 28px;
    line-height: 1.3;
    color: var(--slate);
  }
  .tagline {
    position: absolute;
    left: 0;
    top: 1030px;
    width: 914px;
    text-align: center;
    font-family: "Fira Sans Condensed", sans-serif;
    font-weight: 600;
    font-size: 32px;
    line-height: 1;
    letter-spacing: 2px;
    color: var(--slate);
    text-transform: uppercase;
  }
  .tagline .highlight { color: var(--lime); }
  .site-url {
    position: absolute;
    left: 0;
    top: 1090px;
    width: 914px;
    text-align: center;
    font-family: "Signika", sans-serif;
    font-weight: 500;
    font-size: 24px;
    line-height: 1;
    color: var(--lime);
  }
</style>
</head>
<body>
  <main class="ad">
    <div class="paper" role="img" aria-label="Crumpled, folded sheet of light grey paper"></div>

    <h1 class="brand">plaventro</h1>

    <div class="cloud-art" role="img" aria-label="Outlined cloud icon in slate and lime green"></div>

    <p class="slogan">The cloud you’ve been waiting for,<br>might be closer than you think.</p>

    <p class="tagline">Enterprise SSD Cloud <span class="highlight">with total flexibility</span></p>

    <p class="site-url">www.plaventro.com</p>
  </main>
</body>
</html>
```